Brochure, Stationary and Card Design for Machining and Manufacturing

Keystone Fabrication Inc. requires a package of stationary including a Tri-Fold and Pocket Folder Brochure, Business Card and Letterhead based on the existing branding from our website design and logo.

Keystone Fabrication is a Machine Shop located in Western Canada that specializes in CNC Machining, Electrical Discharge Machining and Rapid Repair Services. Our products are diverse and technically advanced in the oilfield industry. Our Competition is Pellet, Vireo, and Brantwell Oil Tools and the website links are below for your review. Attached is our Website design, logo, pictures, competitor brochures and brochure copy

Our design should be high-tech, professional and should resemble superior quality and customer services. Our website is designed with a HD background picture and we use semi-transparent text boxes to display smaller photos, titles and text. We would like mostly white text and the teal titles as per the colour in the logo. We want a product that can be updated as we make changes to our services by using Photoshop or similar software.

Branding needs to be shared between all the products. Please see our photos and documents attached for inspiration. We will monitor feedback and questions to direct everyone in the right direction.

Attached:

- Pictures to use for background and Titled sections with content. Content to be uploaded soon.
- Sample of existing business card. Add the ISO image to the new card. Brand an all new card from all information.
- Copy of our website design. This is the main inspiration to build around. This site is under construction right now.

www.brantwelloiltools.example **Sample Pics for front of brochure. I like this pic. I will upload pics of our manager like this for you to use to build something inspired by this pic.

www.pelletmachine.example

www.vireomachine.example **Attached a 2 copies of a sample brochure of this competitor.

Target Market(s)

Industrial Purchasers of machining and manufacturing in the oil and gas industry. Down-Hole oil tools, drilling tools, Hydraulic Fracturing and Well Completions.

Industry/Entity Type

Construction

Requirements
Must have
• Business Contact Info:

Keystone Fabrication Inc.
4362-17 Ave NW
Edmonton, AB, T9K 2R4
T: (780) 555-0147
F: (888) 555-0192
Email: info@keystonefab.example

Please add: "ISO 9001-2008 Certification" as part of the logo, text, or the Tellmark ISO image to all items.
Nice to have
• All pictures need touch up and lighting to be corrected. Image 0090 is dark/yellow and needs to be adjusted to be similar colour to other pics.
Should not have
• No background picture on the business card. Keep the card more simplified and clean. Please use the attached ISO logo for the card as well.

```html
<!DOCTYPE html>
<html lang="en">
<head>
<meta charset="utf-8">
<title>Keystone Fabrication – Precision Machined Products Folder</title>
<link rel="stylesheet" href="https://fonts.googleapis.com/css2?family=Exo+2:wght@400;600;700&family=Open+Sans:wght@400;600&display=swap">
<style>
  :root {
    --stage: #d6d6d6;
    --panel: #8f9092;
    --panel-edge: #838486;
    --ink: #111214;
    --teal: #2bb8cc;
    --photo-dark: #3a3d42;
    --photo-mid: #7a7468;
    --photo-light: #b9bcc0;
  }
  * { box-sizing: border-box; margin: 0; padding: 0; }
  html, body { width: 1200px; height: 881px; overflow: hidden; }
  body {
    background: var(--stage);
    font-family: "Open Sans", Arial, sans-serif;
    position: relative;
  }
  .folder {
    position: absolute;
    left: 40px; top: 50px;
    width: 1120px; height: 780px;
    display: flex;
    box-shadow: 0 10px 30px rgba(0,0,0,.25);
  }
  .panel {
    position: relative;
    width: 560px; height: 780px;
    background: var(--panel);
  }
  .panel--back { border-right: 1px solid var(--panel-edge); }

  .brand {
    display: flex; align-items: center; gap: 10px;
    position: absolute;
  }
  .brand__mark {
    width: 26px; height: 26px;
    background: var(--ink);
  }
  .brand__name {
    font-family: "Exo 2", Arial, sans-serif;
    font-weight: 700;
    font-size: 28px;
    letter-spacing: .5px;
    color: var(--ink);
    text-transform: uppercase;
    line-height: 1;
  }

  /* back cover */
  .panel--back .brand { left: 150px; top: 270px; }
  .panel--back .brand__name { font-size: 26px; }
  .contact {
    position: absolute; left: 186px; top: 322px;
    font-size: 9px; line-height: 13px; color: var(--ink);
    font-style: normal;
  }

  /* front cover */
  .panel--front .brand { right: 40px; top: 58px; }
  .hero {
    position: absolute; left: 0; top: 100px;
    width: 560px; height: 300px;
  }
  .headline {
    position: absolute; right: 40px; top: 440px;
    font-family: "Exo 2", Arial, sans-serif;
    font-weight: 600;
    font-size: 44px; line-height: 52px;
    text-align: right;
    text-transform: uppercase;
    color: var(--ink);
    letter-spacing: 1px;
  }
  .cert-badge {
    position: absolute; left: 40px; top: 560px;
    width: 118px; height: 118px;
  }
  .web {
    position: absolute; left: 40px; top: 712px;
    font-size: 13px; color: var(--ink);
  }
</style>
</head>
<body>
  <main class="folder">
    <section class="panel panel--back" aria-label="Back cover">
      <div class="brand">
        <span class="brand__mark"></span>
        <span class="brand__name">Keystone Fabrication</span>
      </div>
      <address class="contact">
        Keystone Fabrication Inc.<br>
        4362-17 Ave NW<br>
        Edmonton, AB, T9K 2R4 Canada<br>
        T: (780) 555-0147<br>
        F: (888) 555-0192<br>
        Email: info@keystonefab.example<br>
        www.keystonemachining.example
      </address>
    </section>

    <section class="panel panel--front" aria-label="Front cover">
      <div class="brand">
        <span class="brand__mark"></span>
        <span class="brand__name">Keystone Fabrication</span>
      </div>

      <svg class="hero" viewBox="0 0 560 300" aria-hidden="false">
        <defs>
          <linearGradient id="heroTone" x1="0" y1="0" x2="1" y2="1">
            <stop offset="0" stop-color="var(--photo-light)"/>
            <stop offset=".45" stop-color="var(--photo-mid)"/>
            <stop offset="1" stop-color="var(--photo-dark)"/>
          </linearGradient>
        </defs>
        <polygon class="hero__frame" points="0,40 120,40 140,26 560,10 560,280 0,230" fill="var(--teal)"/>
        <polygon class="hero__photo" role="img"
          aria-label="Photo of the shop manager with arms crossed beside a bench of machined steel tubes and a CNC monitor"
          points="0,48 124,48 144,34 560,18 560,270 0,222" fill="url(#heroTone)"/>
      </svg>

      <h1 class="headline">Precision Machined<br>Products</h1>

      <svg class="cert-badge" viewBox="0 0 118 118" role="img" aria-label="ISO 9001-2008 registration badge">
        <circle cx="59" cy="59" r="57" fill="var(--ink)"/>
        <circle cx="59" cy="59" r="38" fill="none" stroke="var(--panel)" stroke-width="3"/>
      </svg>

      <p class="web">www.keystonemachining.example</p>
    </section>
  </main>
</body>
</html>
```